LUMO Electrical Services Letter Head

I need a professional clean looking design that will incorporate my company logo and information such as postal address, website, contact email "service@lumoelectrical.com.au" and phone number.

somewhere on the document i will also require my electrical contractor number "EC 047362" and my Australian Business number "57 193 640 208" these have to legally be on the document so they dont need to be a main feature, maybe in the footer in a smaller text.

Can you also have the 3 blue dashes from my logo as the watermark.

I would like the colour scheme to match my logo, business card and website www.lumoelectrical.com.au

I have the JPEG and PNG files for my logo which it will not allow me to upload as they are too wide, if you require these please let me know.

Target Market(s)

To be used for quotes and letters to commercial clients

Industry/Entity Type

Electric Company

Colors
0555a3
3176b5
85acd3
cfdfed
eaf1f7

Requirements
Must have
• company logo and information such as postal address, website, contact email "service@lumoelectrical.com.au" and phone number.
• somewhere on the document i will also require my electrical contractor number "EC 047362" and my Australian Business number "57 193 640 208" these have to legally be on the document so they dont need to be a main feature, maybe in the footer in a smaller text.
• I would like the colour scheme to match my logo, business card and website www.lumoelectrical.com.au
Nice to have
• Can you also have the 3 blue dashes from my logo as the watermark.

```html
<!DOCTYPE html>
<html lang="en">
<head>
<meta charset="utf-8">
<title>LUMO Electrical Services Letterhead</title>
<link rel="stylesheet" href="https://fonts.googleapis.com/css2?family=Montserrat:wght@500;700&display=swap">
<style>
  :root {
    --ink: #231f20;
    --brand-blue: #1d75bc;
    --page-edge: #222222;
    --watermark: #f3f8fb;
    --canvas: #ffffff;
  }
  html, body {
    margin: 0;
    padding: 0;
    width: 1200px;
    height: 1000px;
    overflow: hidden;
    background: var(--canvas);
    font-family: "Montserrat", Arial, sans-serif;
  }
  .letterhead {
    position: absolute;
    left: 263px;
    top: 37px;
    width: 657px;
    height: 930px;
    border: 1px solid var(--page-edge);
    background: var(--canvas);
    overflow: hidden;
  }
  .brand-name {
    position: absolute;
    left: 57px;
    top: 36px;
    margin: 0;
    font-size: 21px;
    font-weight: 700;
    color: var(--ink);
    letter-spacing: 0.2px;
    white-space: nowrap;
  }
  .watermark-band {
    position: absolute;
    left: 0;
    top: 616px;
    width: 657px;
    height: 246px;
    background: linear-gradient(90deg, #f7fafc 0%, var(--watermark) 100%);
  }
  .contact-line {
    position: absolute;
    left: 0;
    right: 0;
    top: 876px;
    display: flex;
    justify-content: center;
    align-items: center;
    gap: 4px;
    font-size: 10.5px;
    font-weight: 500;
    color: var(--ink);
    white-space: nowrap;
  }
  .contact-item {
    display: flex;
    align-items: center;
    gap: 5px;
  }
  .contact-badge {
    width: 19px;
    height: 19px;
    border-radius: 50%;
    background: var(--brand-blue);
    color: #fff;
    font-size: 11px;
    font-weight: 700;
    display: flex;
    align-items: center;
    justify-content: center;
  }
  .legal-line {
    position: absolute;
    left: 0;
    right: 0;
    top: 906px;
    display: flex;
    justify-content: center;
    gap: 19px;
    font-size: 7.5px;
    font-weight: 700;
    color: var(--ink);
    white-space: nowrap;
  }
</style>
</head>
<body>
  <main class="letterhead">
    <header>
      <h1 class="brand-name">LUMO Electrical Services</h1>
    </header>

    <div class="watermark-band" role="img" aria-label="Faint brand watermark area in pale blue"></div>

    <footer>
      <div class="contact-line">
        <span class="contact-item"><span class="contact-badge">A</span>P.O Box 2816, Ridgemont East, WA 6170</span>
        <span class="contact-item"><span class="contact-badge">T</span>(08) 5550 2941</span>
        <span class="contact-item"><span class="contact-badge">E</span>service@lumoelectrical.com.au</span>
      </div>
      <div class="legal-line">
        <span class="contractor-number">EC 047362</span>
        <span class="business-number">Australian Business No. 57 193 640 208</span>
      </div>
    </footer>
  </main>
</body>
</html>
```